Personal training poster - 1200X900mm

Poster to promote my new personal training service at my gym. The poster will be printed and put into an aframe to be seen by people walking past my gym. It needs to be simple and eye catching with the text i have put in the must haves. The text and image should be the prominent parts of the design.

Target Market(s)

30-50 year old females

Industry/Entity Type

Fitness

Font styles to use
Sans Serif

Requirements
Must have
• my logo
• exercise graphic
• Must include the following text:
• Are you looking for a personal trainer? Our expert trainers can help you achieve you take your health and fitness back!
• Contact details:
• 1300452968
• info@brightmovegym.com.au
• Located under the Harbourview Club

```html
<!DOCTYPE html>
<html lang="en">
<head>
<meta charset="utf-8">
<title>Personal Training Poster</title>
<link rel="stylesheet" href="https://fonts.googleapis.com/css2?family=Fredoka:wght@400;500;600&display=swap">
<style>
  :root {
    --page: #ffffff;
    --red: #b03a38;
    --red-deep: #a3302f;
    --lime: #d8e034;
    --blue: #1b5b8e;
    --navy: #1d3f6b;
    --light: #eceaf0;
    --light-pink: #f1dfe2;
    --photo-top: #6e6a70;
    --photo-bottom: #1c1d22;
    --band-text: #e9e33a;
  }
  html, body {
    margin: 0;
    padding: 0;
    width: 1200px;
    height: 1200px;
    overflow: hidden;
    background: var(--page);
  }
  .canvas {
    position: relative;
    width: 1200px;
    height: 1200px;
  }
  .poster {
    position: absolute;
    left: 179px;
    top: 0;
    width: 843px;
    height: 1199px;
    display: block;
  }
  .poster text { font-family: "Fredoka", sans-serif; }
  .headline-small { font-weight: 600; font-size: 64px; fill: var(--blue); }
  .headline-big { font-weight: 600; font-size: 80px; fill: var(--red); }
  .headline-mark { font-weight: 600; font-size: 150px; fill: var(--blue); }
  .sub { font-weight: 600; font-size: 35px; fill: var(--blue); }
  .sub .accent { fill: var(--red); }
  .contact-title { font-weight: 600; font-size: 25px; fill: var(--red); }
  .contact-label { font-weight: 600; font-size: 30px; fill: var(--red); }
  .contact-value { font-weight: 400; fill: var(--red); }
  .brand-name { font-weight: 600; font-size: 26px; fill: var(--blue); }
  .location { font-weight: 600; font-size: 29px; fill: var(--band-text); }
</style>
</head>
<body>
<div class="canvas">
  <svg class="poster" viewBox="0 0 1053 1498" xmlns="http://www.w3.org/2000/svg">
    <defs>
      <linearGradient id="photoTone" x1="0" y1="0" x2="0" y2="1">
        <stop offset="0" stop-color="var(--photo-top)"/>
        <stop offset="0.35" stop-color="#3a3a40"/>
        <stop offset="1" stop-color="var(--photo-bottom)"/>
      </linearGradient>
      <linearGradient id="lightTone" x1="0" y1="0" x2="1" y2="1">
        <stop offset="0" stop-color="#f4f4f6"/>
        <stop offset="0.6" stop-color="var(--light)"/>
        <stop offset="1" stop-color="var(--light-pink)"/>
      </linearGradient>
      <radialGradient id="ghostTone" cx="0.5" cy="0.5" r="0.5">
        <stop offset="0" stop-color="#e7d4d8"/>
        <stop offset="1" stop-color="#e7d4d8" stop-opacity="0"/>
      </radialGradient>
    </defs>

    <rect class="hero-photo" x="0" y="0" width="1053" height="1000" fill="url(#photoTone)"
          role="img" aria-label="Photo of a personal trainer coaching a woman doing suspension strap push-ups in a gym"/>

    <polygon class="light-panel" points="0,1390 1053,660 1053,1498 0,1498" fill="url(#lightTone)"/>
    <ellipse class="ghost-runner" cx="960" cy="1180" rx="210" ry="260" fill="url(#ghostTone)"
             role="img" aria-label="Faded image of a woman running"/>

    <polygon class="red-shape" points="0,505 585,800 1053,505 1053,660 0,1390" fill="var(--red)"/>
    <polygon class="red-stripe" points="1053,428 1053,448 575,795 545,795" fill="var(--red)"/>

    <polygon class="banner-navy" points="235,1012 780,934 782,946 238,1022" fill="var(--navy)"/>
    <polygon class="banner-main" points="140,828 944,717 944,900 140,1020" fill="var(--lime)"/>
    <g transform="rotate(-7.9 140 828)">
      <text class="headline-small" x="178" y="900" textLength="660" lengthAdjust="spacingAndGlyphs">Are you looking for a</text>
      <text class="headline-big" x="158" y="985" textLength="680" lengthAdjust="spacingAndGlyphs">PERSONAL TRAINER</text>
      <text class="headline-mark" x="858" y="990">?</text>
    </g>

    <polygon class="banner-sub" points="234,1022 854,940 854,1090 238,1178" fill="var(--lime)"/>
    <g transform="rotate(-7.6 234 1022)">
      <text class="sub" x="262" y="1070" textLength="565" lengthAdjust="spacingAndGlyphs">Our <tspan class="accent">EXPERT TRAINERS</tspan> can help</text>
      <text class="sub" x="300" y="1114" textLength="495" lengthAdjust="spacingAndGlyphs">you achieve you take your</text>
      <text class="sub" x="312" y="1158" textLength="478" lengthAdjust="spacingAndGlyphs"><tspan class="accent">HEALTH</tspan> and <tspan class="accent">FITNESS</tspan> back</text>
    </g>

    <text class="contact-title" x="192" y="1316">Contact Details</text>
    <text class="contact-label" x="192" y="1356">Call -<tspan class="contact-value">1300452968</tspan></text>
    <text class="contact-label" x="192" y="1394">Email - <tspan class="contact-value">info@brightmovegym.com.au</tspan></text>

    <circle class="brand-dot" cx="908" cy="1318" r="34" fill="var(--blue)"/>
    <text class="brand-name" x="908" y="1388" text-anchor="middle">BrightMove Gym</text>

    <rect class="location-band" x="0" y="1421" width="1053" height="48" fill="var(--red-deep)"/>
    <text class="location" x="192" y="1455">Located under the Harbourview Club</text>
    <rect class="base-strip" x="0" y="1469" width="1053" height="29" fill="#e4e3e8"/>
  </svg>
</div>
</body>
</html>
```